Business Card

I need my new "Advisory" logo incorporated into my existing business card. I want the whole card redesigned. I would like to see a design with the existing colours and a few new colour options. The current card is not elegant or classy enough.

```html
<!DOCTYPE html>
<html lang="en">
<head>
<meta charset="UTF-8">
<title>Business Card – Kestrel Point Group</title>
<link href="https://fonts.googleapis.com/css2?family=Open+Sans:wght@400;600&family=Poppins:wght@400;500;600;700&display=swap" rel="stylesheet">
<style>
  :root {
    --page-bg: #2b2b2d;
    --card-black: #0b0709;
    --card-white: #ffffff;
    --accent: #1aaee0;
    --ink: #2a2a2e;
    --ink-soft: #6b6b70;
    --rule: #3a3a3e;
  }
  * { box-sizing: border-box; margin: 0; padding: 0; }
  html, body { width: 1200px; height: 880px; overflow: hidden; }
  body {
    background: var(--page-bg);
    font-family: "Poppins", sans-serif;
    position: relative;
  }
  .card {
    position: absolute;
    left: 300px;
    width: 600px;
    height: 343px;
    border-radius: 18px;
    overflow: hidden;
  }

  /* Back of card */
  .card-back { top: 70px; background: var(--card-black); }
  .back-brand {
    position: absolute;
    left: 0; right: 0; top: 118px;
    display: flex; flex-direction: column; align-items: center;
    font-family: "Open Sans", sans-serif;
  }
  .back-brand-row { display: flex; align-items: center; gap: 16px; }
  .back-brand-mark {
    width: 46px; height: 46px;
    border: 4px solid var(--accent);
  }
  .back-brand-name {
    color: #ffffff;
    font-weight: 600;
    font-size: 34px;
    letter-spacing: 0.2px;
  }
  .back-tagline {
    margin-top: 6px;
    color: var(--accent);
    font-size: 14px;
    font-weight: 600;
    letter-spacing: 0.4px;
  }

  /* Front of card */
  .card-front { top: 467px; background: var(--card-white); }
  .front-band {
    position: absolute; left: 0; right: 0; bottom: 0;
    height: 12px; background: var(--accent);
  }
  .front-brand {
    position: absolute; left: 40px; top: 112px;
    display: flex; align-items: center; gap: 12px;
  }
  .front-brand-mark {
    width: 50px; height: 50px; border-radius: 50%;
    border: 5px solid var(--accent);
  }
  .front-brand-name {
    font-size: 23px; font-weight: 700; color: var(--ink);
    line-height: 1;
  }
  .front-brand-tagline {
    font-size: 12px; color: var(--ink-soft);
    letter-spacing: 1.4px; margin-top: 5px;
  }
  .rule {
    position: absolute; height: 1px; background: var(--rule);
  }
  .rule-top { left: 300px; right: 40px; top: 62px; }
  .rule-mid { left: 220px; right: 40px; top: 218px; }
  .contact {
    position: absolute; right: 40px; top: 76px;
    text-align: right; font-size: 13px; color: var(--ink);
  }
  .contact-line {
    display: flex; align-items: center; justify-content: flex-end; gap: 8px;
    margin-bottom: 8px;
  }
  .contact-line svg { width: 14px; height: 14px; fill: var(--accent); }
  .person { position: absolute; left: 40px; top: 224px; }
  .person-name { font-size: 20px; font-weight: 600; color: var(--ink); line-height: 1.2; }
  .person-role {
    display: inline-block; margin-top: 4px;
    background: var(--accent); color: #ffffff;
    font-size: 14px; font-weight: 500;
    padding: 2px 26px 2px 8px;
    clip-path: polygon(0 0, 100% 0, 88% 100%, 0 100%);
  }
</style>
</head>
<body>
  <section class="card card-back">
    <div class="back-brand">
      <div class="back-brand-row">
        <div class="back-brand-mark"></div>
        <div class="back-brand-name">Kestrel Point Group</div>
      </div>
      <div class="back-tagline">Seeing well past the horizon line</div>
    </div>
  </section>

  <section class="card card-front">
    <div class="rule rule-top"></div>
    <div class="contact">
      <div class="contact-line">+61 400 123 987
        <svg viewBox="0 0 24 24"><path d="M6.6 10.8a15.1 15.1 0 0 0 6.6 6.6l2.2-2.2a1 1 0 0 1 1-.25 11.4 11.4 0 0 0 3.6.57 1 1 0 0 1 1 1V20a1 1 0 0 1-1 1A17 17 0 0 1 3 4a1 1 0 0 1 1-1h3.5a1 1 0 0 1 1 1c0 1.25.2 2.450.57 3.57a1 1 0 0 1-.25 1z"/></svg>
      </div>
      <div class="contact-line">daniel@kestrelpoint.com.au
        <svg viewBox="0 0 24 24"><path d="M2 5h20v14H2z M4 7v.5l8 5 8-5V7l-8 5z" fill-rule="evenodd"/></svg>
      </div>
    </div>
    <div class="front-brand">
      <div class="front-brand-mark"></div>
      <div>
        <div class="front-brand-name">Meridian Advisory</div>
        <div class="front-brand-tagline">Clear Thinking for Industry</div>
      </div>
    </div>
    <div class="rule rule-mid"></div>
    <div class="person">
      <div class="person-name">Daniel Whitford</div>
      <div class="person-role">Managing Director</div>
    </div>
    <div class="front-band"></div>
  </section>
</body>
</html>
```